I would like alternative creative proposals for our website header at tumbleoakhome.com.au
The current is seen as a bit too drab and dark. We would like to liven it up a bit. The logo will remain although we are open to alternative representation or styling. All submitted designs should include a version that has the existing logo (we do use it within a black circle in other marketing).
The fundamental features of the header must be present including brand logo, search, cart etc.
We want to expand our concept of how the header could appear and function and how it represents our business. Other web site expects will be redesigned to align.
Please become familiar with our business and what we are trying to achieve before submitting a design. We are about health, organic products, chemical free low toxin living, environmental sustainability, all delivered in a modern socially friendly way accessible to all demographics and walks of life with our primary focus on Australia. Our primary target demographic is Australian women between 35 and 55. If you would like more info then please send us some questions.
Development and full design is outside the scoop of this proposal. We are looking for "mockup" proposals for the new website header initially.

```html
<!DOCTYPE html>
<html lang="en">
<head>
<meta charset="utf-8">
<title>Tumble Oak – tumbleoakhome.com.au</title>
<link href="https://fonts.googleapis.com/css2?family=Mulish:wght@400;600;700;800&family=Kaushan+Script&display=swap" rel="stylesheet">
<style>
:root{
  --ink:#1b1b1b;
  --teal:#4a8f9c;
  --mist:#dff0f3;
  --white:#ffffff;
  --coral:#ec6a45;
  --coral-deep:#d0451f;
  --accent:#c9502c;
  --leaf:#3f8f88;
  --black:#000000;
}
*{box-sizing:border-box;margin:0;padding:0}
html,body{width:1200px;height:810px;overflow:hidden;background:var(--white);font-family:"Mulish",sans-serif;color:var(--ink)}
.page{position:relative;width:1200px;height:810px;overflow:hidden}
.top-strip{position:absolute;left:0;top:0;width:1200px;height:6px;background:#2a2a2a}
.utility-bar{position:absolute;left:0;top:6px;width:1200px;height:46px;background:var(--teal)}
.account-links{position:absolute;top:16px;left:596px;font-size:12px;font-weight:700;color:var(--white)}
.account-links span{position:absolute;white-space:nowrap}
.search{position:absolute;left:831px;top:7px;width:243px;height:31px;background:var(--white);border:1px solid #d5d5d5;display:flex;align-items:center;padding:0 10px;font-size:11px;color:#666}
.search svg{position:absolute;right:7px;top:9px}
.brand-band{position:absolute;left:0;top:52px;width:1200px;height:119px;background:var(--mist)}
.brand-box{position:absolute;left:107px;top:6px;width:175px;height:175px;background:var(--black);display:flex;align-items:center;justify-content:center;flex-direction:column;gap:10px;z-index:3}
.brand-box .dot{width:14px;height:14px;border-radius:50%;background:var(--coral)}
.brand-name{font-size:30px;font-weight:800;color:var(--coral);line-height:1;text-align:center;letter-spacing:-0.5px}
.tagline{position:absolute;left:307px;top:68px;font-family:"Kaushan Script",cursive;font-size:24px;color:var(--ink);white-space:nowrap}
.tagline .sep{color:var(--leaf);font-family:"Mulish",sans-serif;font-size:14px;margin:0 6px;vertical-align:middle}
.shop-tools{position:absolute;top:74px;left:770px;font-size:11px;font-weight:700;color:var(--ink)}
.tool{position:absolute;display:flex;align-items:center;gap:5px;white-space:nowrap}
.tool .ico{width:20px;height:20px;border-radius:50%;background:var(--teal);display:flex;align-items:center;justify-content:center}
.main-nav{position:absolute;top:136px;left:305px;font-size:12.5px;font-weight:600;color:var(--ink)}
.main-nav span{position:absolute;white-space:nowrap}
.main-nav .active{color:var(--accent)}
.nav-leaf{position:absolute;left:600px;top:117px}
.hero{position:absolute;left:106px;top:199px;width:972px;height:416px;overflow:hidden;
  background:
    radial-gradient(ellipse 90px 60px at 60px 40px,rgba(230,200,90,.85),transparent 70%),
    radial-gradient(ellipse 110px 70px at 230px 40px,rgba(210,170,70,.8),transparent 70%),
    radial-gradient(ellipse 120px 70px at 370px 50px,rgba(235,210,80,.8),transparent 70%),
    radial-gradient(ellipse 110px 70px at 90px 140px,rgba(160,120,60,.9),transparent 70%),
    radial-gradient(ellipse 120px 70px at 250px 160px,rgba(240,130,40,.9),transparent 70%),
    radial-gradient(ellipse 120px 70px at 400px 170px,rgba(240,200,50,.85),transparent 70%),
    radial-gradient(ellipse 110px 80px at 70px 330px,rgba(200,70,40,.9),transparent 70%),
    radial-gradient(ellipse 120px 80px at 240px 320px,rgba(245,130,35,.95),transparent 70%),
    radial-gradient(ellipse 120px 70px at 400px 300px,rgba(225,205,90,.9),transparent 70%),
    radial-gradient(ellipse 90px 60px at 520px 380px,rgba(170,130,90,.8),transparent 70%),
    radial-gradient(ellipse 120px 90px at 700px 360px,rgba(70,110,60,.9),transparent 70%),
    radial-gradient(ellipse 140px 90px at 880px 330px,rgba(110,150,80,.85),transparent 70%),
    radial-gradient(ellipse 120px 80px at 900px 150px,rgba(90,140,70,.8),transparent 70%),
    radial-gradient(ellipse 100px 60px at 780px 50px,rgba(190,200,190,.6),transparent 70%),
    linear-gradient(100deg,#8a5a2c 0%,#b7834a 30%,#a8773d 48%,#2b342b 50%,#384a36 70%,#243024 100%)}
.hero-divide{position:absolute;left:486px;top:0;width:4px;height:416px;background:rgba(20,25,20,.6)}
.hero-shelf{position:absolute;left:0;width:486px;height:6px;background:rgba(90,80,70,.55)}
.hero-title-plate{position:absolute;left:335px;top:120px;width:327px;height:134px;border-radius:50%;background:rgba(255,255,255,.55)}
.hero-arrow{position:absolute;top:382px}
.dropdown{position:absolute;top:160px;z-index:4;font-size:12px;font-weight:700;color:var(--white)}
.dropdown .col{position:absolute;top:0;width:144px}
.dropdown .col-a{left:552px;background:rgba(236,106,69,.92)}
.dropdown .col-b{left:697px;background:rgba(232,90,55,.96)}
.dropdown .item{height:31px;line-height:31px;padding-left:12px}
.dropdown .item.current{background:var(--coral-deep)}
.tiles{position:absolute;left:0;top:623px}
.tile{position:absolute;width:236px;height:164px;background:var(--black)}
.tile .photo{position:absolute;left:17px;top:11px;width:200px;height:111px}
.tile .label{position:absolute;left:0;top:128px;width:100%;text-align:center;font-size:20px;font-weight:600;color:var(--white);white-space:nowrap;letter-spacing:.3px}
.tile.partial{height:20px;top:172px}
</style>
</head>
<body>
<div class="page">
  <div class="top-strip"></div>
  <header>
    <div class="utility-bar">
      <nav class="account-links">
        <span style="left:0">My Account</span>
        <span style="left:88px">Blog</span>
        <span style="left:132px">Login</span>
        <span style="left:186px">Join</span>
      </nav>
      <div class="search">Search for a product...
        <svg width="12" height="12" viewBox="0 0 12 12"><circle cx="5" cy="5" r="3.6" fill="none" stroke="#444" stroke-width="1.6"/><line x1="7.6" y1="7.6" x2="11" y2="11" stroke="#444" stroke-width="1.8"/></svg>
      </div>
    </div>
    <div class="brand-band"></div>
    <div class="brand-box">
      <span class="dot"></span>
      <div class="brand-name">Tumble<br>Oak</div>
    </div>
    <div class="tagline">Healthy<span class="sep">&#8964;</span>Organic<span class="sep">&#8964;</span>Eco Friendly</div>
    <div class="shop-tools">
      <div class="tool" style="left:0;top:0"><span class="ico"><svg width="10" height="10" viewBox="0 0 10 10"><path d="M1 1 L9 9 M1 1 h3 M1 1 v3 M9 9 h-3 M9 9 v-3" stroke="#fff" stroke-width="1.4" fill="none"/></svg></span>COMPARE</div>
      <div class="tool" style="left:99px;top:0"><span class="ico"><svg width="11" height="10" viewBox="0 0 11 10"><path d="M5.5 9 L1 4.5 A2.3 2.3 0 0 1 5.5 2 A2.3 2.3 0 0 1 10 4.5 Z" fill="#fff"/></svg></span>FAVORITES (0)</div>
      <div class="tool" style="left:217px;top:0"><span class="ico"><svg width="11" height="10" viewBox="0 0 11 10"><path d="M0.5 1 h2 l1.5 5 h5 l1.2-3.5 h-7" stroke="#fff" stroke-width="1.2" fill="none"/><circle cx="4.5" cy="8.3" r="1" fill="#fff"/><circle cx="8.3" cy="8.3" r="1" fill="#fff"/></svg></span>MY CART (0)</div>
    </div>
    <svg class="nav-leaf" width="28" height="12" viewBox="0 0 28 12"><path d="M13 11 C10 4 5 2 1 3 C4 8 8 11 13 11 Z M15 11 C18 4 23 2 27 3 C24 8 20 11 15 11 Z" fill="var(--leaf)"/></svg>
    <nav class="main-nav">
      <span style="left:0">Fresh</span>
      <span style="left:49px">Food &amp; Drink</span>
      <span style="left:140px">Health &amp; Hygiene</span>
      <span class="active" style="left:256px">Skin, Hair &amp; Body</span>
      <span style="left:371px">Mum&amp;Bub</span>
      <span style="left:449px">Yoga&amp;Wellbeing</span>
      <span style="left:561px">Eco Toxin Free Living</span>
      <span style="left:698px">Eco Clothing</span>
    </nav>
  </header>

  <section class="hero" role="img" aria-label="Photo of baskets of organic fruit and a chilled cabinet of fresh vegetables, with a promotional title on a pale oval">
    <div class="hero-shelf" style="top:92px"></div>
    <div class="hero-shelf" style="top:232px"></div>
    <div class="hero-divide"></div>
    <div class="hero-title-plate"></div>
  </section>
  <svg class="hero-arrow" style="left:114px" width="10" height="16" viewBox="0 0 10 16"><path d="M9 1 L2 8 L9 15 Z" fill="#fff"/></svg>
  <svg class="hero-arrow" style="left:1058px" width="10" height="16" viewBox="0 0 10 16"><path d="M1 1 L8 8 L1 15 Z" fill="#fff"/></svg>

  <div class="dropdown">
    <div class="col col-a">
      <div class="item" style="margin-top:3px">Skin Care</div>
      <div class="item">Hair Care</div>
      <div class="item">Cosmetics</div>
      <div class="item">Body Care</div>
      <div class="item" style="height:35px">For Men</div>
    </div>
    <div class="col col-b">
      <div class="item" style="margin-top:3px">Moisturizer</div>
      <div class="item">Cleanser</div>
      <div class="item current">Toner</div>
      <div class="item">Anti-Aging</div>
      <div class="item">Syrum</div>
      <div class="item">Masks</div>
      <div class="item" style="height:35px">Skin Oil</div>
    </div>
  </div>

  <section class="tiles">
    <div class="tile" style="left:109px"><div class="photo" role="img" aria-label="Hands holding a bowl of grain salad on grass" style="background:radial-gradient(ellipse 45px 35px at 140px 45px,#e6dcc2,transparent 75%),radial-gradient(ellipse 80px 30px at 60px 30px,#c7b49a,transparent 75%),linear-gradient(170deg,#9a9a80 0%,#5d9a32 45%,#2f6a1e 100%)"></div><div class="label">Food &amp; Drink</div></div>
    <div class="tile" style="left:353px"><div class="photo" role="img" aria-label="Herbs and flowers beside a small oil bottle on wood" style="background:radial-gradient(ellipse 70px 45px at 80px 45px,#5f9a3a,transparent 75%),radial-gradient(ellipse 25px 20px at 145px 45px,#f3efd8,transparent 75%),radial-gradient(ellipse 30px 25px at 40px 20px,#8a6aa8,transparent 75%),linear-gradient(180deg,#a7b36a 0%,#7a9a48 50%,#c99d62 75%,#8f6a3c 100%)"></div><div class="label">Health &amp; Hygiene</div></div>
    <div class="tile" style="left:596px"><div class="photo" role="img" aria-label="Woman with natural skin in soft green light" style="background:radial-gradient(ellipse 60px 70px at 170px 55px,#edd0b6,transparent 75%),radial-gradient(ellipse 60px 80px at 110px 60px,#d9c08a,transparent 75%),linear-gradient(110deg,#8f9d4a,#b8b772 45%,#e3cdaa)"></div><div class="label">Skin, Hair &amp; Body</div></div>
    <div class="tile" style="left:839px"><div class="photo" role="img" aria-label="Mother holding a baby on a grassy meadow" style="background:radial-gradient(ellipse 40px 45px at 110px 65px,#c9a878,transparent 75%),radial-gradient(ellipse 35px 25px at 100px 95px,#6d7fa8,transparent 75%),linear-gradient(180deg,#9cbc62,#79a542 60%,#5b8a30)"></div><div class="label">Mum &amp; Bub</div></div>
    <div class="tile partial" style="left:109px"></div>
    <div class="tile partial" style="left:353px"></div>
    <div class="tile partial" style="left:596px"></div>
    <div class="tile partial" style="left:839px"></div>
  </section>
</div>
</body>
</html>
```